Double sided flyer for industrial investment firm

We need a A4 double sided flyer (1 page, see attached draft), which we will fold in the midle. Text is attached. What is missing is a professional and clean looking design. Text length can not be changed. it is all in German, but that should not influence the design. The flyer is added to a letter which we send to small industrial companies as an introduction to us as an investor.

What is important?
- No fancy, colorful and funny designs.
- We want a clean, professional almost minimalist design. it does not take much design elements.
- Format either landscape or vertical, whatever works best.
- stay with the colors of our company (grey, blue). see www.velkor-ag.ch for details.
- Currently used graphic in the document should be used, but is not a must. Otherwise stay with pictures or Swiss Alps (if more pictures are needed). will upload some pictures as examples.

Format for the finished flyer: InDesign and Word document or similar.
Updates

The flyer will be folded in the middle so that it becomes A5. all current designs work only as a A4 format. An A4 folded has basically 4 pages, each being A5 size. Please adapt the design accordingly.

Target Market(s)

Owners of small to medium industrial companies in Switzerland

Industry/Entity Type

Industrial

Font styles to use
Serif
Sans Serif

Colors
0255a3
3276b5
85abd2
cedeed

Requirements
Must have
• 1 page, double sided. folded in the middle. A4 Format

```html
<!DOCTYPE html>
<html lang="de">
<head>
<meta charset="utf-8">
<title>Velkor – Fragen und Antworten</title>
<link href="https://fonts.googleapis.com/css2?family=Arimo:wght@400;700&family=Tinos:wght@400;700&display=swap" rel="stylesheet">
<style>
  :root {
    --blue-dark: #0255a3;
    --blue-mid: #3276b5;
    --blue-light: #85abd2;
    --blue-pale: #cedeed;
    --text: #1a1a1a;
    --rule-grey: #6e6e6e;
    --paper: #ffffff;
  }
  * { margin: 0; padding: 0; box-sizing: border-box; }
  html, body {
    width: 1200px; height: 849px; overflow: hidden; background: var(--paper);
  }
  .flyer {
    position: relative; width: 1200px; height: 849px; background: var(--paper);
    font-family: "Arimo", Arial, sans-serif; color: var(--text);
  }
  .hero {
    position: absolute; left: 0; top: 0; width: 1200px; height: 198px;
    background:
      radial-gradient(ellipse at 20% 60%, #9a9a9a 0%, #4a4a4a 45%, #1c1c1c 100%),
      #2a2a2a;
  }
  .hero-shade {
    position: absolute; inset: 0;
    background: linear-gradient(90deg, rgba(0,0,0,0.35) 0%, rgba(255,255,255,0.08) 45%, rgba(0,0,0,0.4) 75%, rgba(255,255,255,0.15) 100%);
  }
  .title-card {
    position: absolute; left: 626px; top: 52px; width: 522px; height: 146px;
    background: var(--paper); border-radius: 10px 10px 0 0;
    display: flex; flex-direction: column; align-items: center;
  }
  .brand {
    margin-top: 38px; display: flex; align-items: center; gap: 12px;
    font-family: "Tinos", "Times New Roman", serif; font-weight: 700;
    font-size: 44px; line-height: 1; color: var(--blue-dark); letter-spacing: 0.5px;
  }
  .brand-mark { width: 18px; height: 18px; background: var(--blue-mid); }
  .title-card .subtitle {
    margin-top: 14px; font-family: "Tinos", "Times New Roman", serif;
    font-weight: 700; font-size: 20px; color: var(--text);
  }
  .header-rule {
    position: absolute; left: 0; top: 198px; width: 1200px; height: 6px; background: var(--rule-grey);
  }
  .column { position: absolute; top: 232px; width: 523px; }
  .column-left { left: 52px; }
  .column-right { left: 626px; }
  .qa h2 {
    font-size: 19.5px; font-weight: 700; line-height: 26px; margin-bottom: 13px;
  }
  .qa p {
    font-size: 15px; line-height: 19.4px; text-align: justify; text-align-last: left;
  }
  .qa + .qa { margin-top: 18px; }
  .column-right .qa + .qa { margin-top: 20px; }
  .footer-rule {
    position: absolute; left: 0; top: 777px; width: 1200px; height: 4px; background: var(--rule-grey);
  }
  .footer-band {
    position: absolute; left: 0; top: 786px; width: 1200px; height: 63px; background: var(--blue-dark);
  }
</style>
</head>
<body>
<main class="flyer">
  <div class="hero" role="img" aria-label="Schwarzweissfoto: Handwerker bearbeitet ein Metallwerkstück in einer Werkstatt">
    <div class="hero-shade"></div>
  </div>
  <header class="title-card">
    <div class="brand"><span class="brand-mark"></span>VELKOR</div>
    <div class="subtitle">Fragen und Antworten zu Velkor</div>
  </header>
  <div class="header-rule"></div>

  <section class="column column-left">
    <article class="qa">
      <h2>Wer sind wir?</h2>
      <p>Wir sind eine Gruppe von ca. 15 Unternehmern, welche unser Kapital in mittelständische Industrieunternehmen investieren mit einem langfristigen Ansatz. Wir haben unser Kapital in der Velkor AG gebündelt und investieren nur in eine kleine Anzahl von Unternehmen. Alle unsere Investoren sind Schweizer mit Wohnsitz in der Schweiz. Wir sind kein Private Equity Fund mit einer definierten Haltedauer und einem Portfolio Ansatz.</p>
    </article>
    <article class="qa">
      <h2>Was ist unser Ziel/Vision?</h2>
      <p>Das Ziel ist nicht Grösse sondern Qualität. Wir wollen eine kleine Industriegruppe aufbauen mit qualitativ hochwertigen Schweizer Industrieunternehmen, welche unabhängig voneinander operieren.</p>
    </article>
    <article class="qa">
      <h2>Welches Kapital investieren wir?</h2>
      <p>Wir investieren unser eigenes Kapital, welches wir über die Jahre aufgebaut haben. Anstatt dieses Kapital an der Börse oder in Immobilien anzulegen, kaufen wir gemeinsam ein Unternehmen und entwickeln dieses. Wir haben mehr Vertrauen in unsere Fähigkeit eine Firma zu entwickeln als in die Finanzmärkte. Einen Teil des Kaufpreises eines Unternehmens finanzieren wir jeweils mit einer Grossbank. Diesen Kredit zahlen wir in der Regel innert 3-4 Jahren zurück, da wir von Banken unabhängig sein wollen.</p>
    </article>
  </section>

  <section class="column column-right">
    <article class="qa">
      <h2>Wie arbeiten wir?</h2>
      <p>Wir sind keine Finanzinvestoren sondern Unternehmer. Der Unterschied liegt in dem intensiven Fokus den wir auf die wenigen Firmen legen, die wir besitzen. Wir wollen unsere Kunden und Märkte im Detail verstehen und so für das Management ein guter<br>Diskussionspartner sein. Das bedingt, dass wir nur sehr wenige Firmen kaufen und diese dann über die Jahre ausbauen im Gegensatz zu einem Finanzinvestor, welcher sich an vielen Unternehmen beteiligt, um sein Risiko zu reduzieren und dann das Unternehmen wieder verkauft.<br>Wir übernehmen operative Aufgaben und leiten gewisse Projekte, damit sich das Management noch besser auf das Tagesgeschäft konzentrieren kann. Diese Arbeiten werden aber immer in Abstimmung mit dem Management ausgeführt, damit jederzeit die Führungsstruktur klar ist.</p>
    </article>
    <article class="qa">
      <h2>Was unterscheidet uns von einem Private Equity Fund?</h2>
      <p>Ein Private Equity Fund kann eine geeignete Finanzierungsquelle für grössere Unternehmen sein. Unternehmer-geführte Mittelständler benötigen die Kombination von Kapital und Führung in Personalunion, um die über die Jahre etablierte Firmenkultur zu bewahren. Ein anonymer Private Equity Fund ist da oft die falsche Lösung. Die Velkor AG als Käufer einer Firma in einer Nachfolgesituation stellt die unternehmerische Kontinuität und Unabhängigkeit auch in Zukunft sicher. Wir sind transparent und langfristig orientiert. Ein Fond verkauft eine Beteiligung normalerweise nach ca. 5 Jahren, wenn der Fond „abläuft“. So eine Frist gibt es bei Velkor nicht.</p>
    </article>
  </section>

  <div class="footer-rule"></div>
  <footer class="footer-band"></footer>
</main>
</body>
</html>
```